Brellin Trade Partners - we are Asian sourcing agents

We are sourcing agents based in the USA and we act as sourcing agents for clients in throughout the world. We focus primarily on custom sewn goods. So basically companies who do not have the in-house expertise to do it themselves, come to us and have us find suitable factories in Asia to do the production. We are middlemen. We find the factories...quote the project...manage the quality control and then deliver the goods directly to our customer's door. We pride ourselves in making the communication very easy and precise.

Current page is www.brellintrade.example

I am not happy w/ the overall look. The spacing...the photos, the fonts...the design elements...the pictures. I want a cool, crisp design that conveys professionalism and clearly depicts/explains what we do.

Requirements
Must have
• use my logo....I like it...it was designed by someone on this website.
Nice to have
• a video/animation of the entire process would be wonderful. Showing initial contact with our office in the USA...then to my correspondence with my offices in Taiwan and in Hong Kong...and then back and fort w/ the customer.....and then between my people in Hong Kong/Taiwan with the local factories......and then a quote is generated and sent to my client......to samples being made and sent for approval.....to a PO being generated......to final samples being sent.....to the order being shipped and delivered to the clients warehouse. I was thinking of an animation showing arrows and text showing the back and forth communication and explaining how the process flows.

```html
<!DOCTYPE html>
<html lang="en">
<head>
<meta charset="utf-8">
<title>Brellin Trade Partners – Asian Outsourcing Made Easy</title>
<link rel="stylesheet" href="https://fonts.googleapis.com/css2?family=Roboto:wght@400;500;700;900&family=Montserrat:wght@400;600&family=Great+Vibes&family=Lora:ital@1&display=swap">
<style>
:root{
  --blue:#0a5ea8;
  --blue-dark:#0b4e8c;
  --navy:#0b2a55;
  --green:#6f8f1c;
  --text:#333;
  --muted:#666;
  --tile:#e3e3e3;
  --tile-ink:#9a9a9a;
  --quote-bg:#e4e4e4;
  --cta-bg:#c9dcec;
  --line:#2c6fb0;
}
*{box-sizing:border-box;margin:0;padding:0}
html,body{width:1200px;height:2278px;overflow:hidden;background:#fff}
body{position:relative;font-family:"Roboto",Arial,sans-serif;color:var(--text)}
.abs{position:absolute}
a{color:inherit;text-decoration:none}

/* header */
.brand{left:106px;top:22px;width:320px}
.brand-name{font-family:"Roboto",sans-serif;font-weight:900;font-size:34px;line-height:1;color:var(--blue-dark);letter-spacing:-.5px}
.call{left:684px;top:22px;font-weight:700;font-size:19px;color:var(--blue-dark)}
.call-phone{left:682px;top:50px;font-size:21px;color:#222;display:flex;align-items:center;gap:8px}
.call-mail{left:874px;top:54px;font-size:15px;color:#222;display:flex;align-items:center;gap:8px}

.nav{left:0;top:95px;width:1200px;height:51px;background:linear-gradient(#1b78c2,#0a5599);display:flex;justify-content:center;gap:46px;align-items:center;padding-left:20px}
.nav a{color:#fff;font-weight:700;font-size:20px}

/* hero */
.headline{left:0;top:178px;width:1200px;text-align:center;font-weight:900;font-size:52px;color:var(--blue)}
.subline{left:0;top:236px;width:1200px;text-align:center;font-size:26px;color:#555}
.hero-photo{left:100px;top:290px;width:631px;height:432px;border:8px solid #fff;box-shadow:0 0 4px rgba(0,0,0,.35);background:linear-gradient(135deg,#7d8a96 0%,#c9ccd0 40%,#5b6673 75%,#3e4650 100%)}
.quote-form{left:756px;top:290px;width:317px;height:432px;border-radius:6px;background:linear-gradient(#fff 0%,#e6edf6 55%,#c7d6e8 100%);box-shadow:0 0 4px rgba(0,0,0,.3);padding:14px 24px}
.quote-form .title{font-family:"Great Vibes",cursive;font-size:30px;color:#333;text-align:center;margin-bottom:6px}
.quote-form label{display:block;font-size:11px;color:#333;margin:10px 0 4px}
.quote-form .field{height:39px;background:#fff;border:1px solid #b9c4d1;position:relative}
.quote-form .submit{margin-top:22px;height:46px;background:linear-gradient(#1c6bb8,#0b4a8a);color:#fff;font-size:20px;display:flex;align-items:center;justify-content:center;border-radius:2px}

.rule{left:99px;width:972px;height:2px;background:var(--line)}
.section-title{left:0;top:743px;width:1200px;text-align:center;font-weight:700;font-size:40px;color:var(--blue)}
.intro{left:110px;top:812px;width:950px;font-size:11px;line-height:15px;color:#555}

/* tiles */
.tile{top:908px;width:221px;height:178px;background:var(--tile);display:flex;flex-direction:column;align-items:center;justify-content:flex-end;padding-bottom:22px;gap:26px;font-size:20px;color:var(--tile-ink)}
.tile.active{background:var(--blue);color:#fff;font-weight:700}

/* link columns */
.col-title{top:1126px;font-weight:700;font-size:26px;color:var(--navy)}
.link-list{top:1192px;list-style:none;font-size:16px;color:var(--blue)}
.link-list li{height:35px}
.contact-text{left:806px;top:1192px;width:260px;font-size:16px;line-height:24px;color:var(--blue)}

/* testimonial */
.testimonial{left:99px;top:1456px;width:970px;height:262px;background:var(--quote-bg)}
.testimonial blockquote{position:absolute;left:176px;top:38px;width:620px;font-family:"Lora",serif;font-style:italic;font-size:13px;line-height:24px;color:#777}
.mark{font-family:"Lora",serif;font-size:56px;color:#c6c6c6;position:absolute}
.avatar{left:515px;top:1615px;width:50px;height:50px;border-radius:50%;background:linear-gradient(#e6c8a8,#b08560);border:2px solid #fff}
.author{left:0;top:1670px;width:1200px;text-align:center;font-size:12px;font-weight:700;color:var(--navy)}
.author span{display:block;font-weight:400;color:#777}

/* call to action */
.cta{left:99px;top:1724px;width:970px;height:175px;background:var(--cta-bg);text-align:center}
.cta h2{margin-top:32px;font-size:31px;font-weight:700;color:var(--blue)}
.cta p{margin-top:6px;font-size:19px;font-weight:700;color:var(--blue)}
.cta .button{position:absolute;left:353px;top:112px;width:270px;height:46px;background:linear-gradient(#1c6bb8,#0b4a8a);color:#fff;font-size:20px;display:flex;align-items:center;justify-content:center}

/* footer */
.footer{left:99px;top:1899px;width:970px;height:322px;background:var(--navy);color:#fff}
.foot-col{position:absolute;top:36px;font-size:10px;line-height:15px}
.foot-col h3{font-family:"Montserrat",sans-serif;font-weight:400;font-size:20px;margin-bottom:18px}
.foot-col ul{list-style:none}
.foot-col li{height:25px;text-transform:uppercase}
.foot-col li.plain{text-transform:none}
.foot-line{display:flex;align-items:center;gap:8px;height:22px}
.socials{display:flex;gap:10px;margin-top:14px}
.socials span{width:28px;height:28px;border-radius:50%;border:2px solid #fff;display:block}
.badge{width:44px;height:16px;background:#fff;margin-top:10px;border-radius:2px}
.copyright{left:0;top:2250px;width:1200px;text-align:center;font-size:10px;color:var(--blue)}
</style>
</head>
<body>

<header>
  <div class="abs brand"><div class="brand-name">BRELLIN TRADE PARTNERS</div></div>
  <div class="abs call">Call us Today</div>
  <div class="abs call-phone">
    <svg width="22" height="22" viewBox="0 0 24 24"><circle cx="12" cy="12" r="11" fill="none" stroke="#222" stroke-width="2"/><path d="M8 6l2 3-1.5 1.5a7 7 0 0 0 5 5L15 14l3 2-1 2.5C11 18 6 13 5.5 7z" fill="#222"/></svg>
    555-014-2290
  </div>
  <div class="abs call-mail">
    <svg width="16" height="12" viewBox="0 0 16 12"><rect width="16" height="12" fill="#222"/><path d="M0 0l8 6 8-6" fill="none" stroke="#fff" stroke-width="1.4"/></svg>
    info@brellintrade.example
  </div>
  <nav class="abs nav"><a>HOME</a><a>PRODUCT CATEGORIES</a><a>ABOUT US</a><a>REQUEST QUOTE</a></nav>
</header>

<main>
  <h1 class="abs headline">ASIAN OUTSOURCING MADE EASY!</h1>
  <p class="abs subline">Custom Sewn Goods Made to Your Specifications</p>

  <div class="abs hero-photo" role="img" aria-label="Photo of a seamstress working at an industrial sewing machine in a factory"></div>

  <form class="abs quote-form">
    <div class="title">Get a free Request Quote!</div>
    <label>Full Name *</label><div class="field"></div>
    <label>Email ID *</label><div class="field"></div>
    <label>Country *</label><div class="field"><svg class="abs" style="right:8px;top:16px" width="6" height="6"><circle cx="3" cy="3" r="2.5" fill="#222"/></svg></div>
    <label>Zip Code</label><div class="field"></div>
    <div class="submit">Request Quote</div>
  </form>

  <div class="abs rule" style="top:736px"></div>
  <h2 class="abs section-title">Sourcing custom goods in China</h2>
  <p class="abs intro">We outsource sewing services direct from China. Our long-established and extensive network of offshore factory-partners provides our clients with access to a wide variety of contract sewing expertise from Chinese manufacturers. Clients only need to communicate with our US agents, but will have the benefits of the cost savings &amp; quality workmanship from offshore outsourcing from Asia.</p>
  <div class="abs rule" style="top:893px"></div>

  <div class="abs tile active" style="left:100px">
    <svg width="70" height="66" viewBox="0 0 70 66" fill="none" stroke="#fff" stroke-width="3.5" stroke-linejoin="round"><rect x="4" y="28" width="14" height="34"/><path d="M18 32l12-14 4-14c5 0 8 4 7 10l-3 10h20c4 0 6 4 5 7l-6 26c-1 3-3 5-6 5H18"/></svg>
    <span>Why Buyer Trust us??</span>
  </div>
  <div class="abs tile" style="left:350px">
    <svg width="70" height="56" viewBox="0 0 70 56" fill="none" stroke="#9a9a9a" stroke-width="3"><path d="M14 3h42l12 16-33 34L2 19z"/><path d="M2 19h66M24 3l-6 16 17 34 17-34-6-16"/></svg>
    <span>Right Product</span>
  </div>
  <div class="abs tile" style="left:599px">
    <svg width="68" height="68" viewBox="0 0 68 68"><circle cx="34" cy="34" r="31" fill="none" stroke="#9a9a9a" stroke-width="4"/><path d="M14 18c8 2 10 8 18 8s6 10 0 14-4 14-8 20c-10-6-16-18-14-30zM40 10c6 4 16 6 18 16-6 2-10 0-14 6-4-4-8-12-4-22z" fill="#9a9a9a"/></svg>
    <span>Right Place</span>
  </div>
  <div class="abs tile" style="left:848px">
    <svg width="64" height="64" viewBox="0 0 64 64" fill="none" stroke="#9a9a9a" stroke-width="3"><path d="M36 4h24v24L28 60 4 36z"/><circle cx="50" cy="14" r="3"/><text x="22" y="44" transform="rotate(-45 30 36)" fill="#9a9a9a" stroke="none" font-family="Roboto,sans-serif" font-size="22" font-weight="700">$</text></svg>
    <span>Right Price</span>
  </div>

  <h3 class="abs col-title" style="left:108px">WHAT YOU NEED TO KNOW</h3>
  <ul class="abs link-list" style="left:110px">
    <li>Contract Sewing in China</li><li>What is the Process?</li><li>What the Minimum Order?</li><li>Contract Outsourcing FAQ</li><li>Outsourcing Case Study</li><li>Custom Industrial Sewing in China</li>
  </ul>
  <h3 class="abs col-title" style="left:477px">SOURCING SOLUTIONS</h3>
  <ul class="abs link-list" style="left:482px;top:1190px">
    <li>Bags</li><li>Cases</li><li>Covers</li><li>Gloves</li><li>Medical</li><li>Sewn Goods</li><li>Sporting Goods</li>
  </ul>
  <h3 class="abs col-title" style="left:801px">REQUEST A QUOTE</h3>
  <div class="abs contact-text">
    Please contact us for immediate consultation regarding your outsourcing project.<br><br>
    Tel: 555-014-2290<br>Fax: 555-014-2291<br>Email: info@brellintrade.example
  </div>

  <section class="abs testimonial">
    <span class="mark" style="left:100px;top:4px">“</span>
    <blockquote>Brellin Trade Partners have been a reliable, efficient supplier over the years, sourcing products for our company, working with our required branding, specific labelling and facilitating logistics from within China to ship into Australia. We highly recommend working with Brellin Trade and plan to continue our supplier relationship for years to come.</blockquote>
    <span class="mark" style="left:830px;top:98px">”</span>
  </section>
  <div class="abs avatar" role="img" aria-label="Customer portrait"></div>
  <div class="abs author">Marcus Reede<span>Bay Area, SanFrancisco</span></div>

  <section class="abs cta">
    <h2>Outsource Your Sewing Needs to Trusted Contractors in China</h2>
    <p>Please contact us for immediate consultation regarding your outsourcing project.</p>
    <div class="button">Request Quote</div>
  </section>
</main>

<footer class="abs footer">
  <div class="foot-col" style="left:19px;width:150px">
    <h3>About Us</h3>
    <p>Lorem ipsum dolor sit amet, consectetur adipiscing elit. Vivamus sit amet ligula vel diam congue semper.</p><br>
    <p>Lorem ipsum dolor sit amet, consectetur adipiscing elit. Vivamus sit amet ligula vel diam conguem ipsum dolor sit ame. consectetur adipiscing elit. Vivamus sit amet ligula.<br>vel diam congue semper.</p>
  </div>
  <div class="foot-col" style="left:248px;width:180px">
    <h3>Contact Us</h3>
    <p>US HEADQUARTERS<br>Brellin Trade Partners<br>40 Harbor Lane<br>Suite B-2<br>Easton, NH 03000</p><br>
    <div class="foot-line"><svg width="10" height="8"><rect width="10" height="8" fill="#fff"/></svg>info@brellintrade.example</div>
    <div class="foot-line"><svg width="10" height="10"><circle cx="5" cy="5" r="5" fill="#fff"/></svg>555-014-2290</div>
    <div class="foot-line"><svg width="10" height="10"><rect width="10" height="10" fill="#fff"/></svg>555-014-2291</div>
  </div>
  <div class="foot-col" style="left:499px;width:200px">
    <h3>Quick Links</h3>
    <ul>
      <li class="plain">About Us</li><li>Custom Bags</li><li>Custom Covers</li><li>Custom Medical Accessories</li><li>Custom Sewn Goods</li><li>Custom Cases</li><li>Custom Gloves</li><li>Custom Sporting Goods</li><li class="plain">Terms and Conditions</li>
    </ul>
  </div>
  <div class="foot-col" style="left:748px;width:200px">
    <h3>Stay in Touch!</h3>
    <p>Follow US in our social networks!<br>Lorem ipsum dolor sit amet, consectetur and go adipiscing elit.</p>
    <div class="socials"><span></span><span></span><span></span><span></span></div>
    <div class="badge"></div>
  </div>
</footer>
<p class="abs copyright">© Brellin Trade Partners, LLC | USA - Hong Kong - Taipei</p>

</body>
</html>
```